cartNest - a stylish trolley for apartments

We neede a simple website to sell our Trolley, for apartment use.
The colour theme is red, blask & white. Our logo is attached and this needs to be on the Home page.
The website only needs a Home Page plus 4 other pges.
In the attachment you will find a site map.

You can check out the following two sites to see what I like:
www.plinthgallery.example/design-showcase-inspiration/minimalist-portfolio-website/
www.brightquarry.example/inspiration/40-beautiful-web-design-portfolios/ in this site especially
Dario Menezes
K B Forge
Nine 17 Studio
Oliver Marsh

And especially Lamp - I ike the simpicity of the site esp as we are only selling one product

Target Market(s)

Apartment dwellers

Industry/Entity Type

Apartment

Requirements
Must have
• This website must have 4 pages.
We need Corvo, Ledgerline and Quidly portals.
Order Form for Trolley
Payment form.

```html
<!DOCTYPE html>
<html lang="en">
<head>
<meta charset="utf-8">
<title>cartNest – a stylish trolley for apartments</title>
<link href="https://fonts.googleapis.com/css2?family=Open+Sans:wght@400;600&display=swap" rel="stylesheet">
<style>
:root{
  --red:#d0121b;
  --ink:#222;
  --panel:#f2f2f2;
  --frame:#4a4a4a;
  --white:#fff;
  --grey-text:#444;
}
*{box-sizing:border-box;margin:0;padding:0}
html,body{width:816px;height:1200px;overflow:hidden;background:var(--white);font-family:'Open Sans',sans-serif;color:var(--ink)}
.page{position:relative;width:816px;height:1200px}
.abs{position:absolute}

.brand{left:44px;top:8px;width:126px;height:96px;border-radius:63px 63px 0 0;background:#eeeeee}
.brand-name{left:54px;top:106px;font-size:21px;font-weight:600;color:var(--red);display:flex;align-items:center;gap:6px;z-index:2}
.brand-name .dot{width:10px;height:10px;border-radius:50%;background:#f2c300}

.account{right:144px;top:14px;font-size:11px;color:var(--grey-text);display:flex;gap:6px;align-items:center}
.account .items{color:var(--red)}
.checkout{left:712px;top:10px;width:67px;height:23px;border-radius:8px;background:#444;color:#fff;font-size:11px;display:flex;align-items:center;justify-content:center}
.contact{right:37px;font-size:12.5px;text-align:right}
.contact span{color:var(--red);font-size:11px;margin-right:5px}

.nav{left:25px;top:99px;width:762px;height:45px;background:var(--panel);border-bottom:3px solid #444}
.nav-links{left:185px;top:113px;display:flex;gap:26px;font-size:12.5px}
.nav-links a{color:var(--ink);text-decoration:none;display:flex;align-items:center;gap:6px}
.nav-links i{display:inline-flex;gap:2px}
.nav-links i::before,.nav-links i::after{content:"";width:5px;height:5px;border-radius:50%;background:var(--red)}
.order{left:657px;top:99px;width:130px;height:43px;background:var(--red);color:#fff;font-weight:600;font-size:13px;display:flex;align-items:center;justify-content:center}

.slider{left:25px;top:147px;width:764px;height:407px;border:5px solid var(--frame);background:linear-gradient(90deg,#9c9c9a 0%,#d9d9d6 25%,#b8b6ad 50%,#dedcd5 75%,#8f8e8a 100%)}
.slider-floor{left:30px;top:430px;width:754px;height:119px;background:linear-gradient(180deg,#2c2c2c,#55543d)}
.slide-dots{left:698px;top:532px;display:flex;gap:4px}
.slide-dots b{width:10px;height:10px;border-radius:50%;background:#fff}
.slide-dots b:first-child{background:#f2d200}

.content{left:25px;top:554px;width:765px;height:562px;background:var(--panel)}
.copy{left:41px;top:576px;width:735px;font-size:11.3px;line-height:16.7px;color:#333;text-align:justify}
.copy p{margin-bottom:16.7px}
.copy .name{color:var(--red)}
.list{left:96px;top:713px;font-size:11.3px;font-weight:600;line-height:19px;list-style:none}
.list li{display:flex;align-items:center;gap:10px}
.list li::before{content:"";border-left:6px solid var(--red);border-top:5px solid transparent;border-bottom:5px solid transparent}
.headline{left:25px;top:762px;width:765px;text-align:center;font-size:25px;font-weight:400;color:var(--red)}
.headline b{font-weight:400;color:var(--ink)}

.arch{top:825px;width:240px;height:272px;border-radius:120px 120px 0 0;background:#fff;border:1px solid #d0d0d0;padding:4px}
.arch div{width:100%;height:100%;border-radius:116px 116px 0 0}

.social{left:788px;width:22px;height:22px;background:var(--red);border-radius:2px}

.footer{left:25px;top:1115px;width:765px;height:70px;background:linear-gradient(180deg,#7a7a7a,#2a2a2a)}
.foot-links{left:37px;top:1125px;font-size:11.5px;color:#f0f0f0;display:flex;gap:8px}
.accept{left:540px;top:1123px;font-size:11.5px;font-weight:600;color:#fff}
.cards{left:607px;top:1124px;display:flex;gap:10px}
.cards span{width:27px;height:16px;background:#fff;border-radius:2px;font-size:5px;color:#333;display:flex;align-items:center;justify-content:center}
.copyright{right:28px;top:1164px;font-size:9.5px;color:#eee}
</style>
</head>
<body>
<div class="page">
  <div class="abs brand"></div>

  <div class="abs account">My Account <span>|</span> Shopping cart
    <svg width="16" height="13" viewBox="0 0 16 13"><path d="M1 1h2.5l2 8h8l1.5-6H5" fill="none" stroke="#444" stroke-width="1.2"/><circle cx="6.5" cy="11.5" r="1" fill="#444"/><circle cx="12.5" cy="11.5" r="1" fill="#444"/></svg>
    <span class="items">(0) items</span></div>
  <div class="abs checkout">Check out</div>
  <div class="abs contact" style="top:57px"><span>Call</span>0800 – 55120478</div>
  <div class="abs contact" style="top:76px"><span>Email</span>customer@cartnest.example</div>

  <div class="abs nav"></div>
  <div class="abs brand-name"><span class="dot"></span>cartNest</div>
  <nav class="abs nav-links">
    <a href="#"><i></i>cartNest</a>
    <a href="#"><i></i>Gallery</a>
    <a href="#"><i></i>Contact Us</a>
  </nav>
  <div class="abs order">Order cartNest</div>

  <div class="abs slider" role="img" aria-label="Chrome luggage trolley with red suitcases and hanging garments beside steel lift doors"></div>
  <div class="abs slider-floor" aria-hidden="true"></div>
  <svg class="abs" style="left:43px;top:324px" width="44" height="44" viewBox="0 0 44 44"><circle cx="22" cy="22" r="21" fill="rgba(255,255,255,.7)" stroke="#333"/><path d="M30 8 12 22l18 14" fill="none" stroke="var(--red)" stroke-width="1.2"/></svg>
  <svg class="abs" style="left:732px;top:302px" width="44" height="44" viewBox="0 0 44 44"><circle cx="22" cy="22" r="21" fill="rgba(255,255,255,.7)" stroke="#333"/><path d="M14 8l18 14-18 14" fill="none" stroke="var(--red)" stroke-width="1.2"/></svg>
  <div class="abs slide-dots"><b></b><b></b><b></b><b></b><b></b></div>

  <div class="abs content"></div>
  <div class="abs copy">
    <p><span class="name">cart</span>Nest originated from our personal experience of apartment living, and the hassle of taking shopping, luggage, etc, from your car to your apartment. We have sourced trolleys from all over the place, and failed to find a versatile, strong trolley, which also looked stylish. Our emphasis is on style because we wanted a trolley which would sit inside our front door, and look great! We are busy people and wanted a trolley, at hand.! We were tired of trolleys which had to be packed up and put in cupboards. This action continuously weakened the trolleys and parts broke easily due to the” wear and tear”.</p>
    <p>Most domestic trolleys are not strong, and nearly always look like they belong in a factory or workshop. We decided that we wanted a trolley that:</p>
  </div>
  <ul class="abs list">
    <li>Looked attractive living anywhere in our apartment, and not inside a cupboard</li>
    <li>Offered both hanging and flat-bed options.</li>
  </ul>
  <h1 class="abs headline">So ... we welcome cart<b>Nest</b> to the marketplace!</h1>

  <div class="abs arch" style="left:33px"><div role="img" aria-label="Man loading a garment bag onto the trolley in a car park" style="background:linear-gradient(160deg,#b8a060,#6a6a5a 50%,#3a3a3a)"></div></div>
  <div class="abs arch" style="left:286px"><div role="img" aria-label="Couple handing over shopping beside a loaded trolley" style="background:linear-gradient(160deg,#8a8a80,#4a4a55 50%,#2a2a40)"></div></div>
  <div class="abs arch" style="left:542px"><div role="img" aria-label="Man standing beside the trolley in an apartment lobby" style="background:linear-gradient(160deg,#50606a,#a0a8a8 50%,#5a6870)"></div></div>

  <a href="#" class="abs social" style="top:576px" aria-label="Social page one"></a>
  <a href="#" class="abs social" style="top:606px" aria-label="Social page two"></a>

  <div class="abs footer"></div>
  <div class="abs foot-links"><span>cartNest</span><span>|</span><span>Gallery</span><span>|</span><span>Contact Us</span></div>
  <div class="abs accept">We accept</div>
  <div class="abs cards"><span>Corvo</span><span>Quidly</span><span>Roamer</span><span>Ledgerline</span><span>Meridian</span></div>
  <div class="abs copyright">Copyright 2012 cartNest. All rights reserved.</div>
</div>
</body>
</html>
```